Stationery Design Project for Bramble Co

Hi All,

We need you to design stationary for a new online financial services business. We have already got the logo designed and it is attached. If you would like it in any other formats please let me know. If you could also if possible, match the fonts in your design to that on the logo’s provided.

What we need:
- Business Card
- A4 Letter head
- A4 Folders
- PPT template (Title page and regular page)

And what ever else you want to throw in.

We are in the process of getting the web site designed, however below is a list of websites which we like which will give you an understanding of the style that we are going for.

- plimo.com
- brambleroute.com
- tallowquay.com
- pelkwintry.com

I look forward to your seeing your design.

Industry/Entity Type

Financial

Requirements
Must have
• Outputs:
- Documents ready to print
- Generic editable information
- Pdf copies of the documents
- Word version of letterhead

```html
<!DOCTYPE html>
<html lang="en">
<head>
<meta charset="utf-8">
<title>Bramble Co stationery</title>
<link rel="stylesheet" href="https://fonts.googleapis.com/css2?family=Open+Sans:wght@400;600;700&family=Archivo:wght@700;800&display=swap">
<style>
  :root {
    --bg: #c6c6c6;
    --blue: #1180aa;
    --orange: #f7941d;
    --orange-deep: #f26522;
    --yellow: #fbb03b;
    --navy: #0e2a47;
    --ink: #333333;
    --white: #ffffff;
  }
  * { box-sizing: border-box; margin: 0; padding: 0; }
  html, body { width: 1200px; height: 944px; overflow: hidden; background: var(--bg); }
  body { position: relative; font-family: "Open Sans", Arial, sans-serif; color: var(--ink); }
  .piece { position: absolute; box-shadow: 1px 2px 4px rgba(0,0,0,.3); overflow: hidden; }

  .brand-name { font-family: "Open Sans", Arial, sans-serif; font-weight: 600; letter-spacing: -.01em; white-space: nowrap; }
  .brand-dot { display: inline-block; border-radius: 50%; background: var(--orange); vertical-align: middle; }

  .decor { position: absolute; background: linear-gradient(135deg, var(--yellow), var(--orange) 55%, var(--orange-deep)); }

  /* business card front */
  .card-front { left: 135px; top: 298px; width: 259px; height: 144px; background: var(--blue); }
  .card-front .decor { left: 0; top: 0; width: 142px; height: 144px; border-radius: 0 72px 72px 0; }
  .card-front .brand-name { position: absolute; left: 157px; top: 58px; font-size: 21px; color: var(--white); }

  /* business card back */
  .card-back { left: 135px; top: 482px; width: 259px; height: 144px; background: var(--white); }
  .card-back .stripe { position: absolute; left: 0; top: 0; width: 12px; height: 100%; background: var(--blue); }
  .card-back .brand { position: absolute; left: 29px; top: 17px; display: flex; align-items: center; gap: 6px; }
  .card-back .brand-dot { width: 20px; height: 20px; }
  .card-back .brand-name { font-size: 15px; color: var(--navy); }
  .card-back .person { position: absolute; left: 60px; top: 73px; }
  .card-back .person-name { font-size: 9.5px; color: var(--ink); line-height: 1.1; }
  .card-back .person-role { font-size: 8px; color: var(--orange-deep); line-height: 1.1; }
  .card-back .contact { position: absolute; left: 60px; top: 110px; font-size: 6.6px; line-height: 1.3; color: #555; }

  /* title slide */
  .slide-title { left: 462px; top: 36px; width: 589px; height: 417px; background: var(--blue); }
  .slide-title .header { position: absolute; left: 0; top: 0; width: 100%; height: 108px; background: var(--white); display: flex; align-items: center; justify-content: center; gap: 14px; }
  .slide-title .brand-dot { width: 46px; height: 46px; }
  .slide-title .brand-name { font-size: 34px; color: var(--navy); }
  .slide-title .decor { left: 0; top: 108px; width: 268px; height: 309px; border-radius: 0 268px 0 0; }
  .slide-title .heading { position: absolute; left: 265px; top: 168px; font-family: "Archivo", Arial, sans-serif; font-weight: 800; font-size: 35px; line-height: 1; color: var(--white); }
  .slide-title .subheading { position: absolute; left: 266px; top: 250px; font-size: 19px; letter-spacing: .04em; color: var(--white); }

  /* content slide */
  .slide-content { left: 462px; top: 494px; width: 588px; height: 416px; background: var(--white); }
  .slide-content .header { position: absolute; left: 0; top: 0; width: 100%; height: 74px; background: var(--blue); }
  .slide-content .decor { left: 0; top: 0; width: 72px; height: 74px; border-radius: 0 37px 37px 0; }
  .slide-content .page-title { position: absolute; left: 96px; top: 22px; font-family: "Archivo", Arial, sans-serif; font-weight: 700; font-size: 27px; line-height: 1; color: var(--white); }
  .slide-content .brand-name { position: absolute; right: 24px; top: 20px; font-size: 25px; color: var(--white); }
  .slide-content .body { position: absolute; left: 36px; top: 112px; width: 530px; }
  .slide-content h2 { font-size: 23px; font-weight: 600; color: var(--blue); margin-bottom: 6px; }
  .slide-content .point { font-size: 14.5px; line-height: 1.25; color: var(--ink); }
  .slide-content .point::before { content: "• "; }
  .slide-content ul { list-style: none; margin: 4px 0 10px 98px; }
  .slide-content li { font-size: 10.8px; line-height: 18px; color: var(--blue); white-space: nowrap; }
  .slide-content li::before { content: "- "; }
  .slide-content ul.accent li { color: var(--orange-deep); }
</style>
</head>
<body>

<section class="piece card-front">
  <div class="decor" role="img" aria-label="Orange brand decoration on blue"></div>
  <span class="brand-name">bramble</span>
</section>

<section class="piece card-back">
  <div class="stripe"></div>
  <div class="brand"><span class="brand-dot"></span><span class="brand-name">brambleco.com</span></div>
  <div class="person">
    <p class="person-name">Owen Rask</p>
    <p class="person-role">manager</p>
  </div>
  <div class="contact">
    <p>City, State Name, 31 StreetName str</p>
    <p>Phone: 555-014-2270 • Fax: 555-014-2271</p>
    <p>owen@brambleco.com • www.brambleco.com</p>
  </div>
</section>

<section class="piece slide-title">
  <div class="header"><span class="brand-dot"></span><span class="brand-name">bramble</span></div>
  <div class="decor" role="img" aria-label="Large orange brand decoration"></div>
  <h1 class="heading">PRESENTATION<br>TITLE</h1>
  <p class="subheading">SUBTITLE</p>
</section>

<section class="piece slide-content">
  <div class="header">
    <div class="decor" role="img" aria-label="Orange brand decoration"></div>
    <p class="page-title">TITLE NAME</p>
    <span class="brand-name">brambleco.com</span>
  </div>
  <div class="body">
    <h2>Sample text</h2>
    <p class="point">Sample text, sample text Sample text, sample textSample text, sample text</p>
    <ul>
      <li>Sample text, sample text Sample text, sample textSample text, sample text</li>
      <li>Sample text, sample text Sample text, sample textSample text, sample text</li>
      <li>Sample text, sample text Sample text, sample textSample text, sample text</li>
    </ul>
    <p class="point">Sample text, sample textSample text, sample textSample text, sample text</p>
    <ul class="accent">
      <li>Sample text, sample text Sample text, sample textSample text, sample text</li>
      <li>Sample text, sample text Sample text, sample textSample text, sample text</li>
    </ul>
    <p class="point">Sample text, sample text Sample text, sample textSample text, sample text</p>
    <ul>
      <li>Sample text, sample text Sample text, sample textSample text, sample text</li>
      <li>Sample text, sample text Sample text, sample textSample text, sample text</li>
      <li>Sample text, sample text Sample text, sample textSample text, sample text</li>
    </ul>
  </div>
</section>

</body>
</html>
```